Review/Re-Design Supermarket E-Commerce website

We have launched our Supermarket E-commerce Website but feel it is lacking a modern feel.

Please re-design the current Supermarket E-commerce site, creating a more modern look and feel.

I am looking for design changes to things such as:

- Fonts
- Button shape & Size
- Shapes of boxes
- Layout of drop down menus
- A new shopping cart / button
- The Header (and in particular the use and positioning of the logo)
- Supplying a generic background image (currently berries)

Please do not change the structure of the page. For instance, the category selection will always be on the left, the items will always be displayed in rows of 3 and the shopping cart should be on the right.
Updates

Current site can be found at www.brovanmarket.com.au

Project Deadline Extended
Reason: designs coming in are generally too different from current design. we are looking for less that 10% change to the overall look and feel. one aspect that needs a lot of work is the checkout cart on the right hand side. please checkout http://www2.pelkinfreshmart.com.au/?gclid=QXRP4kdmwnLBHTYEzJuaPGEKtB

Target Market(s)

Consumers buying their weekly grocery shopping online

Industry/Entity Type

Shopping

Number of Pages Required

1 page

Requirements
Must have
• Stick to the branding of the Logo. Which is Red, Blue and White.
• Other colours may be used in small percentages.
Should not have
• Do not change the Structure of the site.

```html
<!DOCTYPE html>
<html lang="en">
<head>
<meta charset="utf-8">
<title>Brovan Market – Apples</title>
<link rel="stylesheet" href="https://fonts.googleapis.com/css2?family=Roboto:wght@400;500;700&family=Roboto+Condensed:wght@400;700&display=swap">
<style>
:root{
  --red:#e8202e;
  --red-dark:#b9151f;
  --blue:#1a63b4;
  --blue-dark:#114a8a;
  --green:#1f6b3a;
  --grey-band:#efefef;
  --grey-light:#f4f4f4;
  --grey-line:#d8d8d8;
  --pink-line:#f3b6bb;
  --text:#333;
  --footer:#f1f0ee;
}
*{box-sizing:border-box;margin:0;padding:0}
html,body{width:1200px;height:2282px;overflow:hidden;background:#fff}
body{position:relative;font-family:"Roboto",Arial,sans-serif;color:var(--text)}
.abs{position:absolute}
a{color:inherit;text-decoration:none}

/* header */
.header{left:0;top:0;width:1200px;height:155px;background:#fff}
.phone{left:110px;top:12px;display:flex;align-items:center;gap:14px;font-size:20px;color:#222}
.brand{left:110px;top:58px;font-family:"Roboto Condensed",Arial,sans-serif;font-weight:700;font-size:40px;color:var(--blue);display:flex;align-items:center;gap:14px;letter-spacing:1px}
.brand-dot{width:26px;height:26px;border-radius:50%;background:var(--red)}
.btn-small{top:28px;height:30px;border:1px solid #9fb2c4;border-radius:3px;font-size:11px;display:flex;align-items:center;justify-content:center;color:#333;background:#fff}
.currency{left:860px;top:36px;font-size:11px;color:#333}
.search{left:685px;top:80px;width:280px;height:38px;background:#eee}
.search-btn{left:965px;top:80px;width:48px;height:38px;background:var(--green);display:flex;align-items:center;justify-content:center}
.cart-tab{left:1037px;top:0;width:78px;height:142px}
.cart-count{left:1037px;top:16px;width:78px;text-align:center;color:#fff;font-size:20px}

/* nav */
.nav{left:0;top:155px;width:1200px;height:60px;background:var(--blue)}
.nav ul{list-style:none;display:flex;position:absolute;left:110px;top:0;height:60px}
.nav li{width:201px;height:60px;display:flex;align-items:center;justify-content:center;color:#fff;font-size:12px;border-right:1px solid rgba(255,255,255,.6)}
.nav li:first-child{background:var(--red)}
.nav li:last-child{border-right:1px solid rgba(255,255,255,.6)}

/* hero */
.hero{left:0;top:215px;width:1200px;height:548px;background:
  radial-gradient(ellipse at 25% 40%,#d9342a 0,#c44a2a 18%,transparent 40%),
  radial-gradient(ellipse at 78% 25%,#a8c84a 0,#8db33a 20%,transparent 45%),
  radial-gradient(ellipse at 70% 78%,#f3a12a 0,#e98a1e 20%,transparent 42%),
  linear-gradient(180deg,#6b8a3a 0,#9a5a2a 45%,#e6e2dc 100%)}
.hero-title{left:0;width:1200px;text-align:center;font-family:"Roboto",Arial,sans-serif;line-height:1;letter-spacing:2px}
.t-always{top:295px;font-size:78px;color:rgba(60,110,220,.75);font-weight:400}
.t-fresh{top:380px;font-size:80px;color:var(--green);font-weight:700}
.t-fruits{top:465px;font-size:80px;color:var(--red);font-weight:400}
.hero-sub{left:0;top:563px;width:1200px;text-align:center;color:#fff;font-size:24px;line-height:30px;text-transform:uppercase}
.shop-now{left:525px;top:640px;width:205px;height:64px;background:var(--blue);color:#fff;font-size:22px;font-weight:500;display:flex;align-items:center;justify-content:center;gap:12px;box-shadow:0 2px 4px rgba(0,0,0,.3)}

/* toolbar */
.toolbar{left:0;top:763px;width:1200px;height:77px;background:var(--grey-band)}
.specials{left:110px;top:763px;width:255px;height:77px;background:var(--blue);color:#fff;font-size:19px;display:flex;align-items:center;justify-content:center}
.select{top:782px;height:36px;background:#fff;border:1px solid #ccc;font-size:10px;display:flex;align-items:center;padding-left:14px}
.select .caret{position:absolute;right:0;top:-1px;width:36px;height:36px;background:var(--blue);display:flex;align-items:center;justify-content:center}
.collect{left:810px;top:780px;display:flex;gap:10px;font-size:10px;line-height:13px;color:#333}
.delivery{left:990px;top:789px;display:flex;align-items:center;gap:10px;font-size:10px;color:#333;border-left:1px solid #ccc;padding-left:10px;height:30px}

/* breadcrumb */
.crumbs{left:395px;top:840px;width:805px;height:32px;background:var(--grey-light);font-size:13px;color:#555;padding:8px 8px}

/* sidebar */
.cat-head{left:110px;top:840px;width:255px;height:78px;background:var(--red);color:#fff;font-size:18px;display:flex;align-items:center;justify-content:center;gap:12px}
.cat-head .drop{position:absolute;right:20px;top:33px}
.sub-list{left:110px;top:918px;width:255px;list-style:none;border:1px solid var(--grey-line)}
.sub-list li{height:42px;border-bottom:1px solid #c9d6e6;background:#f2f2f2;color:var(--blue);font-size:13px;padding:14px 0 0 33px;position:relative}
.cat-list{left:110px;top:1130px;width:255px;list-style:none;border:1px solid var(--pink-line)}
.cat-list li{height:33px;border-bottom:1px solid var(--pink-line);background:#ececec;color:var(--red);font-size:13px;padding:9px 0 0 8px;position:relative;text-transform:uppercase}
.arrow{position:absolute;right:14px;top:50%;margin-top:-5px;width:0;height:0;border-left:8px solid currentColor;border-top:5px solid transparent;border-bottom:5px solid transparent}

/* products */
.card{width:208px;height:328px;border:1px solid #e2e2e2;background:#fff}
.card .photo{position:absolute;left:8px;top:8px;width:190px;height:166px;border:1px solid #e6e6e6;background:#fff;display:flex;align-items:center;justify-content:center}
.fruit{width:110px;height:110px;border-radius:50%}
.card .name{position:absolute;left:0;top:198px;width:100%;text-align:center;font-size:11px;color:var(--blue)}
.card .price{position:absolute;left:0;top:222px;width:100%;text-align:center;font-size:24px;color:#222}
.card .each{position:absolute;left:0;top:252px;width:100%;text-align:center;font-size:14px;color:#444}
.add{position:absolute;left:6px;top:273px;width:110px;height:32px;background:var(--red);color:#fff;font-size:10px;display:flex;align-items:center;padding-left:8px}
.add .ico{position:absolute;right:0;top:0;width:30px;height:32px;background:var(--red-dark);display:flex;align-items:center;justify-content:center}
.qty{position:absolute;left:130px;top:273px;width:62px;height:32px;background:var(--blue);color:#fff;font-size:10px;display:flex;align-items:center;padding-left:8px}
.qty b{position:absolute;right:0;top:0;width:26px;height:32px;background:var(--blue-dark);font-weight:400;font-size:14px;display:flex;align-items:center;justify-content:center}

/* footer */
.footer{left:0;top:1960px;width:1200px;height:322px;background:var(--footer);border-top:2px solid #cfcfcf}
.f-text{font-size:13px;color:#222;line-height:24px}
.app-badge{left:148px;top:2015px;width:135px;height:45px;background:#111;border-radius:5px}
.mobile-badge{left:148px;top:2063px;width:135px;height:45px;background:#fff;border:2px solid #111;border-radius:5px;font-size:12px;line-height:14px;text-align:center;padding-top:7px}
.pay{top:2196px;height:30px;border-radius:4px}
.divider{top:1977px;width:1px;height:195px;background:#333}
.social{top:1977px;width:36px;height:36px;border-radius:50%;background:#111}
.copy{left:190px;top:2247px;font-size:13px;color:#222}
</style>
</head>
<body>

<!-- header -->
<header class="abs header">
  <div class="abs phone">
    <svg width="24" height="24" viewBox="0 0 24 24" aria-hidden="true"><path d="M6.6 10.8a15.1 15.1 0 0 0 6.6 6.6l2.2-2.2c.3-.3.7-.4 1-.2 1.1.4 2.3.6 3.6.6.6 0 1 .4 1 1V20c0 .6-.4 1-1 1A17 17 0 0 1 3 4c0-.6.4-1 1-1h3.5c.6 0 1 .4 1 1 0 1.3.2 2.5.6 3.6.1.3 0 .7-.2 1z" fill="#111"/></svg>
    <span>1300 555 019</span>
  </div>
  <div class="abs brand"><span>BROVAN MARKET</span><span class="brand-dot"></span></div>

  <a class="abs btn-small" style="left:685px;width:62px">SIGN IN</a>
  <a class="abs btn-small" style="left:770px;width:75px">REGISTER</a>
  <div class="abs currency">CURRENCIES: &nbsp;US DOLLAR</div>
  <div class="abs search"></div>
  <div class="abs search-btn">
    <svg width="20" height="20" viewBox="0 0 20 20" aria-hidden="true"><circle cx="8" cy="8" r="6" fill="none" stroke="#fff" stroke-width="2.5"/><line x1="12.5" y1="12.5" x2="18" y2="18" stroke="#fff" stroke-width="3"/></svg>
  </div>
  <svg class="abs cart-tab" viewBox="0 0 78 142" aria-hidden="true">
    <polygon points="0,0 78,0 78,142 40,128 0,128" fill="#e8202e"/>
    <path d="M18 66h8l8 34h30l6-24H30" fill="none" stroke="#fff" stroke-width="5"/>
    <circle cx="38" cy="110" r="5" fill="#fff"/><circle cx="60" cy="110" r="5" fill="#fff"/>
  </svg>
  <div class="abs cart-count">0</div>
</header>

<nav class="abs nav">
  <ul>
    <li>HOME</li><li>ABOUT US</li><li>PRODUCTS</li><li>MY CART</li><li>CONTACTS</li>
  </ul>
</nav>

<!-- hero -->
<section class="abs hero" role="img" aria-label="Photograph of fresh fruit: apples, strawberries, grapes, kiwi and sliced orange on white"></section>
<div class="abs hero-title t-always">ALWAYS</div>
<div class="abs hero-title t-fresh">FRESH</div>
<div class="abs hero-title t-fruits">FRUITS</div>
<p class="abs hero-sub">Aliquam dapibus tincidunt metus. Praesent justo dolor<br>lobortis quis, lobortis...</p>
<a class="abs shop-now">SHOP NOW!
  <svg width="30" height="28" viewBox="0 0 30 28" aria-hidden="true"><path d="M1 3h5l4 16h14l4-11H8" fill="none" stroke="#fff" stroke-width="3"/><circle cx="12" cy="24" r="2.5" fill="#fff"/><circle cx="22" cy="24" r="2.5" fill="#fff"/></svg>
</a>

<!-- toolbar -->
<div class="abs toolbar"></div>
<div class="abs specials">ONLINE SPECIALS</div>
<div class="abs select" style="left:398px;width:147px">FILTER BY<span class="caret"><svg width="14" height="9" viewBox="0 0 14 9"><polygon points="0,0 14,0 7,9" fill="#fff"/></svg></span></div>
<div class="abs select" style="left:560px;width:146px">SORT BY<span class="caret"><svg width="14" height="9" viewBox="0 0 14 9"><polygon points="0,0 14,0 7,9" fill="#fff"/></svg></span></div>
<div class="abs collect">
  <svg width="22" height="30" viewBox="0 0 22 30" aria-hidden="true"><path d="M11 1a8 8 0 0 0-8 8c0 6 8 15 8 15s8-9 8-15a8 8 0 0 0-8-8z" fill="#222"/><circle cx="11" cy="9" r="3" fill="#fff"/></svg>
  <span>Click&amp;Collect<br>4/12-18 Marlow Street Ashby<br>TAS 72</span>
</div>
<div class="abs delivery">
  <svg width="32" height="20" viewBox="0 0 32 20" aria-hidden="true"><rect x="1" y="2" width="18" height="12" fill="#222"/><path d="M19 6h7l5 5v3H19z" fill="#222"/><circle cx="7" cy="16" r="3" fill="#222"/><circle cx="25" cy="16" r="3" fill="#222"/></svg>
  <span>Delivery Info</span>
</div>

<div class="abs crumbs">Home &nbsp;/ &nbsp;Fruit &nbsp;/ &nbsp;Apples</div>

<!-- sidebar -->
<div class="abs cat-head">
  <svg width="22" height="20" viewBox="0 0 22 20" aria-hidden="true"><path d="M1 2h4l3 11h10l3-8H6" fill="none" stroke="#fff" stroke-width="2.4"/><circle cx="9" cy="17" r="2" fill="#fff"/><circle cx="17" cy="17" r="2" fill="#fff"/></svg>
  BABY
  <svg class="drop" width="14" height="10" viewBox="0 0 14 10"><polygon points="0,0 14,0 7,10" fill="#fff"/></svg>
</div>
<ul class="abs sub-list">
  <li>ACCESSORIES<span class="arrow"></span></li>
  <li>BABY FOOD<span class="arrow"></span></li>
  <li>BABY OIL<span class="arrow"></span></li>
  <li>BATH TIME<span class="arrow"></span></li>
  <li>CHANGE TIME<span class="arrow"></span></li>
</ul>
<ul class="abs cat-list">
  <li>Baking Needs<span class="arrow"></span></li>
  <li>Beverages<span class="arrow"></span></li>
  <li>Biscuits<span class="arrow"></span></li>
  <li>Breakfast Foods<span class="arrow"></span></li>
  <li>Caned Food<span class="arrow"></span></li>
  <li>Cheese<span class="arrow"></span></li>
  <li>Chilled Foods<span class="arrow"></span></li>
  <li>Chips<span class="arrow"></span></li>
  <li>Condiments<span class="arrow"></span></li>
  <li>Confectionery<span class="arrow"></span></li>
  <li>Cooking Needs, Season..<span class="arrow"></span></li>
  <li>Desserts<span class="arrow"></span></li>
  <li>Frozen Food<span class="arrow"></span></li>
  <li>Fruit<span class="arrow"></span></li>
  <li>Hardware &amp; Outdoor<span class="arrow"></span></li>
  <li>Health Foods<span class="arrow"></span></li>
  <li>Homewares<span class="arrow"></span></li>
  <li>Household Cleaning<span class="arrow"></span></li>
  <li>International Foods<span class="arrow"></span></li>
  <li>Jams &amp; Spreads<span class="arrow"></span></li>
</ul>

<!-- products -->
<article class="abs card" style="left:393px;top:890px">
  <div class="photo"><div class="fruit" role="img" aria-label="Bag of small red apples" style="background:radial-gradient(circle at 40% 35%,#ff5a5a,#c4101e 60%,#7a0a12)"></div></div>
  <p class="name">APPLES RED 2KG BAG</p><p class="price">$8.39</p><p class="each">$8.39 EA</p>
  <div class="add">ADD TO CART<span class="ico"><svg width="18" height="16" viewBox="0 0 18 16"><path d="M1 2h3l2 8h9l2-6H5" fill="none" stroke="#fff" stroke-width="2"/><circle cx="7" cy="14" r="1.6" fill="#fff"/><circle cx="14" cy="14" r="1.6" fill="#fff"/></svg></span></div>
  <div class="qty">QTY<b>0</b></div>
</article>
<article class="abs card" style="left:640px;top:890px">
  <div class="photo"><div class="fruit" role="img" aria-label="Red and yellow apple" style="background:radial-gradient(circle at 40% 35%,#e9a07a,#b4323a 60%,#6e1a20)"></div></div>
  <p class="name">APPLES RED 2KG BAG</p><p class="price">$8.39</p><p class="each">$8.39 EA</p>
  <div class="add">ADD TO CART<span class="ico"><svg width="18" height="16" viewBox="0 0 18 16"><path d="M1 2h3l2 8h9l2-6H5" fill="none" stroke="#fff" stroke-width="2"/><circle cx="7" cy="14" r="1.6" fill="#fff"/><circle cx="14" cy="14" r="1.6" fill="#fff"/></svg></span></div>
  <div class="qty">QTY<b>0</b></div>
</article>
<article class="abs card" style="left:888px;top:890px">
  <div class="photo"><div class="fruit" role="img" aria-label="Green apple with leaf" style="background:radial-gradient(circle at 40% 35%,#a8e05a,#4fae1e 60%,#2a6e10)"></div></div>
  <p class="name">APPLES RED 2KG BAG</p><p class="price">$8.39</p><p class="each">$8.39 EA</p>
  <div class="add">ADD TO CART<span class="ico"><svg width="18" height="16" viewBox="0 0 18 16"><path d="M1 2h3l2 8h9l2-6H5" fill="none" stroke="#fff" stroke-width="2"/><circle cx="7" cy="14" r="1.6" fill="#fff"/><circle cx="14" cy="14" r="1.6" fill="#fff"/></svg></span></div>
  <div class="qty">QTY<b>0</b></div>
</article>

<article class="abs card" style="left:393px;top:1245px">
  <div class="photo"><div class="fruit" role="img" aria-label="Deep red apple" style="background:radial-gradient(circle at 40% 35%,#f0506a,#c0102e 60%,#6a0616)"></div></div>
  <p class="name">APPLES RED 2KG BAG</p><p class="price">$8.39</p><p class="each">$8.39 EA</p>
  <div class="add">ADD TO CART<span class="ico"><svg width="18" height="16" viewBox="0 0 18 16"><path d="M1 2h3l2 8h9l2-6H5" fill="none" stroke="#fff" stroke-width="2"/><circle cx="7" cy="14" r="1.6" fill="#fff"/><circle cx="14" cy="14" r="1.6" fill="#fff"/></svg></span></div>
  <div class="qty">QTY<b>0</b></div>
</article>
<article class="abs card" style="left:640px;top:1245px">
  <div class="photo"><div class="fruit" role="img" aria-label="Red and golden apple" style="background:radial-gradient(circle at 40% 35%,#f5c44a,#e07a2a 55%,#b4302a)"></div></div>
  <p class="name">APPLES RED 2KG BAG</p><p class="price">$8.39</p><p class="each">$8.39 EA</p>
  <div class="add">ADD TO CART<span class="ico"><svg width="18" height="16" viewBox="0 0 18 16"><path d="M1 2h3l2 8h9l2-6H5" fill="none" stroke="#fff" stroke-width="2"/><circle cx="7" cy="14" r="1.6" fill="#fff"/><circle cx="14" cy="14" r="1.6" fill="#fff"/></svg></span></div>
  <div class="qty">QTY<b>0</b></div>
</article>
<article class="abs card" style="left:888px;top:1245px">
  <div class="photo"><div class="fruit" role="img" aria-label="Pile of light green apples" style="background:radial-gradient(circle at 40% 35%,#e4f28a,#b6d44a 60%,#7e9e22)"></div></div>
  <p class="name">APPLES RED 2KG BAG</p><p class="price">$8.39</p><p class="each">$8.39 EA</p>
  <div class="add">ADD TO CART<span class="ico"><svg width="18" height="16" viewBox="0 0 18 16"><path d="M1 2h3l2 8h9l2-6H5" fill="none" stroke="#fff" stroke-width="2"/><circle cx="7" cy="14" r="1.6" fill="#fff"/><circle cx="14" cy="14" r="1.6" fill="#fff"/></svg></span></div>
  <div class="qty">QTY<b>0</b></div>
</article>

<article class="abs card" style="left:393px;top:1603px">
  <div class="photo"><div class="fruit" role="img" aria-label="Yellow apple" style="background:radial-gradient(circle at 40% 35%,#fbe08a,#e8b63a 60%,#b07a1a)"></div></div>
  <p class="name">APPLES RED 2KG BAG</p><p class="price">$8.39</p><p class="each">$8.39 EA</p>
  <div class="add">ADD TO CART<span class="ico"><svg width="18" height="16" viewBox="0 0 18 16"><path d="M1 2h3l2 8h9l2-6H5" fill="none" stroke="#fff" stroke-width="2"/><circle cx="7" cy="14" r="1.6" fill="#fff"/><circle cx="14" cy="14" r="1.6" fill="#fff"/></svg></span></div>
  <div class="qty">QTY<b>0</b></div>
</article>

<!-- footer -->
<footer class="abs footer"></footer>
<p class="abs f-text" style="left:148px;top:1973px">Download Our App</p>
<div class="abs app-badge" role="img" aria-label="App download badge"></div>
<div class="abs mobile-badge">Mobile site<br>Available</div>
<p class="abs f-text" style="left:148px;top:2150px">We accept</p>
<div class="abs pay" style="left:148px;width:46px;background:#555" role="img" aria-label="Payment card"></div>
<div class="abs pay" style="left:202px;width:46px;background:#333" role="img" aria-label="Payment card"></div>
<div class="abs pay" style="left:258px;width:30px;border-radius:50%;background:#b8962a" role="img" aria-label="Secure payment seal"></div>

<ul class="abs f-text" style="left:395px;top:1973px;list-style:none">
  <li>My Account</li><li>My Past Orders</li><li>Online Specials</li><li>Everyday Specials</li>
</ul>
<ul class="abs f-text" style="left:395px;top:2123px;list-style:none">
  <li>About Queuely</li><li>About Us</li>
</ul>
<div class="abs divider" style="left:532px"></div>
<ul class="abs f-text" style="left:560px;top:1973px;list-style:none">
  <li>Delivery</li><li>FAQ</li><li>Privacy Policy</li><li>Terms &amp; Conditions</li>
</ul>
<ul class="abs f-text" style="left:560px;top:2123px;list-style:none">
  <li>Contact us</li><li>1300 555 019</li>
</ul>
<div class="abs divider" style="left:697px"></div>
<p class="abs f-text" style="left:725px;top:1973px">End User License<br>Agreement</p>
<div class="abs social" style="left:890px" role="img" aria-label="Social link"></div>
<div class="abs social" style="left:946px" role="img" aria-label="Social link"></div>
<div class="abs social" style="left:1002px" role="img" aria-label="Social link"></div>
<p class="abs copy">© Queuely Pty Ltd 2014 - All Rights Reserved <small style="font-size:8px">v1.12</small></p>

</body>
</html>
```